Breakfast Briefings / Lunch & Learn

I would like to have a double sided flyer size 8x10 to display the breakfast briefing on one side and Lunch & Learn on the other side.

Header on each side to say
2018 Calendar Breakfast Briefing (on the breakfast side)
2018 Calendar Lunch & Learn (on the lunch side)

I have attached a copy of the files we would like to use.

Industry/Entity Type

Learn

Colors

Designer to choose colors to be used in the design.

```html
<!DOCTYPE html>
<html lang="en">
<head>
<meta charset="utf-8">
<title>2018 Calendar – Breakfast Briefing / Lunch &amp; Learn</title>
<link href="https://fonts.googleapis.com/css2?family=Montserrat:wght@400;600;700&family=Raleway:wght@400;500&display=swap" rel="stylesheet">
<style>
:root{
  --bg:#e9e6e2;
  --paper:#ffffff;
  --blue:#1670ab;
  --blue-dark:#17659c;
  --blue-light:#3d9cd6;
  --grey-text:#3f3f3f;
  --band:#ececec;
  --sky:#6cbbd9;
  --rule:#9a9a9a;
}
*{margin:0;padding:0;box-sizing:border-box}
html,body{width:1200px;height:1200px;overflow:hidden;background:var(--bg)}
.stage{position:absolute;left:0;top:0;width:1500px;height:1500px;transform:scale(.8);transform-origin:0 0}
.flyer{position:absolute;top:314px;width:697px;height:871px;background:var(--paper);box-shadow:0 4px 18px rgba(0,0,0,.18);overflow:hidden}
.flyer--breakfast{left:36px}
.flyer--lunch{left:768px}
.title-year{font-family:"Montserrat",sans-serif;font-weight:700;color:var(--blue);font-size:47px;line-height:1}
.title-name{font-family:"Raleway",sans-serif;font-weight:400;color:var(--grey-text);font-size:50px;line-height:1;margin-top:8px}
.flyer--breakfast .heading{position:absolute;top:38px;left:0;width:100%;text-align:center}
.ring{position:absolute;left:0;top:0}
.ring text{font-family:"Montserrat",sans-serif;fill:#fff;font-size:10.5px;text-anchor:middle}
.ring .month{font-weight:700}
.url{position:absolute;top:826px;font-family:"Montserrat",sans-serif;font-size:15px;letter-spacing:9px;color:#333}
.flyer--breakfast .url{left:0;width:100%;text-align:center}
.flyer--breakfast .url-rule{position:absolute;top:836px;height:1px;background:var(--rule);width:165px}
.url-rule--left{left:42px}.url-rule--right{right:42px}
.lunch-main{position:absolute;left:0;top:0;width:388px;height:100%}
.flyer--lunch .heading{position:absolute;left:39px;top:36px}
.flyer--lunch .title-name{font-size:50px}
.topics{position:absolute;left:40px;top:173px;width:335px;list-style:none}
.topic{height:51.8px}
.topic-month{font-family:"Montserrat",sans-serif;font-weight:600;font-size:14.5px;color:var(--blue);padding-left:20px;position:relative;height:20px;line-height:20px}
.topic-month::before{content:"";position:absolute;left:2px;top:4px;width:2.5px;height:13px;background:var(--blue);box-shadow:5px 0 0 var(--blue)}
.topic-title{background:var(--band);font-family:"Raleway",sans-serif;font-weight:500;font-size:15.5px;color:#333;padding-left:20px;height:21px;line-height:21px}
.brand{position:absolute;left:0;width:100%;top:762px;text-align:center;font-family:"Raleway",sans-serif;font-weight:500;font-size:34px;letter-spacing:6px;color:#444}
.flyer--lunch .url{left:0;width:388px;text-align:center}
.lunch-side{position:absolute;left:388px;top:0;width:309px;height:100%}
.side-sky{position:absolute;left:0;top:0;width:100%;height:446px;background:var(--sky)}
.side-illustration{position:absolute;left:30px;top:76px;width:240px;height:240px;border-radius:50%;background:radial-gradient(circle,#f4f8fb 0 52%,#3a5966 53% 62%,#8fcbe2 63%)}
.side-lettering{position:absolute;left:48px;top:348px;width:224px;height:34px;border-radius:4px;background:linear-gradient(90deg,rgba(240,200,90,.55),rgba(240,200,90,.25))}
.side-photo{position:absolute;left:0;top:446px;width:100%;height:425px;background:radial-gradient(ellipse at 30% 25%,#f3b45c,#c2723a 45%,#5a2a14 90%)}
.side-and{position:absolute;left:0;width:100%;top:392px;text-align:center;font-family:"Montserrat",sans-serif;font-weight:700;font-size:92px;color:#fff;line-height:1;text-shadow:0 0 0 var(--sky),3px 3px 0 #5aa9c9}
</style>
</head>
<body>
<div class="stage">

  <section class="flyer flyer--breakfast">
    <header class="heading">
      <div class="title-year">2018 Calendar</div>
      <div class="title-name">Breakfast Briefing</div>
    </header>

    <svg class="ring" width="697" height="871" viewBox="0 0 697 871">
      <defs>
        <marker id="head-dark" markerWidth="4" markerHeight="4" refX="1.5" refY="2" orient="auto"><path d="M0,0 L4,2 L0,4 Z" fill="var(--blue-dark)"/></marker>
        <marker id="head-light" markerWidth="4" markerHeight="4" refX="1.5" refY="2" orient="auto"><path d="M0,0 L4,2 L0,4 Z" fill="var(--blue-light)"/></marker>
        <path id="orbit-arrow" d="M -54.5 -256.3 A 262 262 0 0 1 72.2 -251.9" fill="none" stroke-width="7"/>
        <radialGradient id="table-tone" cx="50%" cy="50%" r="60%">
          <stop offset="0" stop-color="#f6efe6"/><stop offset=".32" stop-color="#b15a18"/><stop offset=".4" stop-color="#5b3a26"/><stop offset="1" stop-color="#3e291d"/>
        </radialGradient>
      </defs>

      <g transform="translate(347 481)">
        <use href="#orbit-arrow" stroke="var(--blue-dark)" marker-end="url(#head-dark)"/>
        <use href="#orbit-arrow" transform="rotate(30)" stroke="var(--blue-light)" marker-end="url(#head-light)"/>
        <use href="#orbit-arrow" transform="rotate(60)" stroke="var(--blue-light)" marker-end="url(#head-light)"/>
        <use href="#orbit-arrow" transform="rotate(90)" stroke="var(--blue-dark)" marker-end="url(#head-dark)"/>
        <use href="#orbit-arrow" transform="rotate(120)" stroke="var(--blue-dark)" marker-end="url(#head-dark)"/>
        <use href="#orbit-arrow" transform="rotate(150)" stroke="var(--blue-dark)" marker-end="url(#head-dark)"/>
        <use href="#orbit-arrow" transform="rotate(180)" stroke="var(--blue-dark)" marker-end="url(#head-dark)"/>
        <use href="#orbit-arrow" transform="rotate(210)" stroke="var(--blue-light)" marker-end="url(#head-light)"/>
        <use href="#orbit-arrow" transform="rotate(240)" stroke="var(--blue-light)" marker-end="url(#head-light)"/>
        <use href="#orbit-arrow" transform="rotate(270)" stroke="var(--blue-dark)" marker-end="url(#head-dark)"/>
        <use href="#orbit-arrow" transform="rotate(300)" stroke="var(--blue-dark)" marker-end="url(#head-dark)"/>
        <use href="#orbit-arrow" transform="rotate(330)" stroke="var(--blue-dark)" marker-end="url(#head-dark)"/>

        <circle r="141" fill="none" stroke="var(--blue-light)" stroke-width="2"/>
        <circle r="134" fill="url(#table-tone)" role="img" aria-label="Photo: cup of tea and pretzel on a wooden table with a brand tag"/>
      </g>

      <g class="dept">
        <g transform="translate(347 243)"><circle r="52" fill="var(--blue-dark)"/><circle r="46" fill="none" stroke="#fff" stroke-width="1.3"/>
          <text y="-20">Medical</text><text y="-5">Dana Caldwell</text><text y="10">2019</text><text y="25" class="month">TBD</text></g>
        <g transform="translate(467 281)"><circle r="52" fill="var(--blue-light)"/><circle r="46" fill="none" stroke="#fff" stroke-width="1.3"/>
          <text y="-20">Sales</text><text y="-5">Jon Alvarez</text><text y="10">2019</text><text y="25" class="month">TBD</text></g>
        <g transform="translate(554 366)"><circle r="52" fill="var(--blue-light)"/><circle r="46" fill="none" stroke="#fff" stroke-width="1.3"/>
          <text y="-12">Finance</text><text y="3">Rob Carlin</text><text y="18" class="month">MARCH</text></g>
        <g transform="translate(584 483)"><circle r="52" fill="var(--blue-dark)"/><circle r="46" fill="none" stroke="#fff" stroke-width="1.3"/>
          <text y="-20">R&amp;D</text><text y="-5">Chris</text><text y="10">Christakos</text><text y="25" class="month">APRIL</text></g>
        <g transform="translate(554 603)"><circle r="52" fill="var(--blue-dark)"/><circle r="46" fill="none" stroke="#fff" stroke-width="1.3"/>
          <text y="-12">Operations</text><text y="3">Peter Schultz</text><text y="18" class="month">MAY</text></g>
        <g transform="translate(464 691)"><circle r="52" fill="var(--blue-dark)"/><circle r="46" fill="none" stroke="#fff" stroke-width="1.3"/>
          <text y="-12">Clinical/ Reg</text><text y="3">Ben Glover</text><text y="18" class="month">JUNE</text></g>
        <g transform="translate(349 721)"><circle r="52" fill="var(--blue-dark)"/><circle r="46" fill="none" stroke="#fff" stroke-width="1.3"/>
          <text y="-20">Quality</text><text y="-5">Doug</text><text y="10">Allenby</text><text y="25" class="month">JULY</text></g>
        <g transform="translate(231 684)"><circle r="52" fill="var(--blue-light)"/><circle r="46" fill="none" stroke="#fff" stroke-width="1.3"/>
          <text y="-12">People</text><text y="3">Diya Ghosh</text><text y="18" class="month">AUGUST</text></g>
        <g transform="translate(144 596)"><circle r="52" fill="var(--blue-light)"/><circle r="46" fill="none" stroke="#fff" stroke-width="1.3"/>
          <text y="-12">Marketing</text><text y="3">Neel Tandon</text><text y="18" class="month">SEPTEMBER</text></g>
        <g transform="translate(112 483)"><circle r="52" fill="var(--blue-dark)"/><circle r="46" fill="none" stroke="#fff" stroke-width="1.3"/>
          <text y="-12">Legal</text><text y="3">Kamal Rafiq</text><text y="18" class="month">OCTOBER</text></g>
        <g transform="translate(146 366)"><circle r="52" fill="var(--blue-dark)"/><circle r="46" fill="none" stroke="#fff" stroke-width="1.3"/>
          <text y="-20">Market Access</text><text y="-6">Kathryn</text><text y="8">Neumann</text><text y="22" class="month">NOVEMBER</text></g>
        <g transform="translate(232 276)"><circle r="52" fill="var(--blue-dark)"/><circle r="46" fill="none" stroke="#fff" stroke-width="1.3"/>
          <text y="-12">TOS</text><text y="3">Clara Smyth</text><text y="18" class="month">DECEMBER</text></g>
      </g>
    </svg>

    <span class="url-rule url-rule--left"></span>
    <div class="url">WWW.VANTORA.COM</div>
    <span class="url-rule url-rule--right"></span>
  </section>

  <section class="flyer flyer--lunch">
    <div class="lunch-main">
      <header class="heading">
        <div class="title-year">2018 Calendar</div>
        <div class="title-name">Lunch &amp; Learn</div>
      </header>
      <ul class="topics">
        <li class="topic"><div class="topic-month">MARCH:</div><div class="topic-title">Mindfulness</div></li>
        <li class="topic"><div class="topic-month">APRIL:</div><div class="topic-title">Nutrition and Lifestyle Coaching</div></li>
        <li class="topic"><div class="topic-month">MAY:</div><div class="topic-title">What is Neuromodulation?</div></li>
        <li class="topic"><div class="topic-month">JUNE:</div><div class="topic-title">Achieve Your Goals</div></li>
        <li class="topic"><div class="topic-month">JULY:</div><div class="topic-title">Changing Your LifePositive Thinking</div></li>
        <li class="topic"><div class="topic-month">AUGUST:</div><div class="topic-title">Clean EatingHow Do I Get Started</div></li>
        <li class="topic"><div class="topic-month">SEPTEMBER:</div><div class="topic-title">Budgeting 101 Financial Wellness</div></li>
        <li class="topic"><div class="topic-month">OCTOBER:</div><div class="topic-title">Busted! Nutrition Myths</div></li>
        <li class="topic"><div class="topic-month">NOVEMBER:</div><div class="topic-title">Time Management</div></li>
        <li class="topic"><div class="topic-month">DECEMBER:</div><div class="topic-title">First Time Home Buyers</div></li>
      </ul>
      <div class="brand">vantora</div>
      <div class="url">WWW.VANTORA.COM</div>
    </div>

    <aside class="lunch-side">
      <div class="side-sky"></div>
      <div class="side-illustration" role="img" aria-label="Illustration: two students at laptops inside a ring of learning icons with the word Learn"></div>
      <div class="side-lettering" role="img" aria-label="Hand lettering: Life. Long. Learn"></div>
      <div class="side-photo" role="img" aria-label="Photo: warmly lit restaurant table with glasses and cutlery"></div>
      <div class="side-and">AND</div>
    </aside>
  </section>

</div>
</body>
</html>
```